Velmora Trade Hall (front page)

We need a design of a front page for our Velmora Trade Hall website (vth.co.uk). Our company is based in the United Kingdom and offers investors from all over the world an opportunity to invest into bitcoin and litecoin.

We have been developing this cutting edge technology for past 2 years based on our in depth knowledge on conventional stock and currency trading technology and methodology. We have run many test against penetration, security and stability and now are ready to deploy.

Recent news about vulnerability of such platforms leave a great deal of unease from retail investors about investing into cryptocurrency. We are set to challenge this attitude. Our background is payments in particular regulated environment in the UK. We are keen to apply our wealth of experience to provide secure and reliable trading platform and advance cryptocurrency as means of legal tender.

The front page should be based on the feel and look of our current technology vth.co.uk. Some of you have already been involved in logo design for our company, please see the attached mockups. The page should have this minimalist design, very clean and light.

Seek inspiration form www.korvelin.net, www.trusmarq.com, vip.plomwerth.com and other bitcoin exchanges.

We look forward to receiving your ideas.

You can also refer to our social pages:
https://www.facebook.com/vth.co.uk
https://twitter.com/vth_uk

We would like you to focus your efforts at designing the page in such a way so that it is very easy for visitor be open an account with the exchange. We must focus at informing the visitor about the bitcoin, how to my buy, how to sell, look at the general overview of the maker and CONVERTING him/her sing up. This is the most important!!

Regards,
Oren

Reason: Dear all, We are very keen on getting this design done right the first time. The key success is conversion of visitors to subscribers and then to traders. It is absolutely essential make the registration process as streamlined as possible! When we are calling them to act by "Change the world one bitcoin at a time" we should give them a opportunity to provide us with relevant account creation details: email, password, confirm password. Please visit quenzo.co.uk for ideas. Secondly, tell them what is a bitcoin, why a bitcoin is a good investment and how to invest. Finally, it is important to inform visitors of "who we are", what sets us apart from other exchanges, tell them about our experience. In our view graphs and live order books are important but they might turn some visitors away especially the ones that are not accustomed to online trading. Think of what would you like to see on the page if you wanted YOURSELF to invest. What would make you to create an account and use it? Think what will work, we are here to revolutionise how people do business.... any wild ideas put them to us. OUR BUDGET JUST GONE UP!!!

Target Market(s)

A combination of professional and consumer bitcoin investors.

Requirements
Must have
• News section

```html
<!DOCTYPE html>
<html lang="en">
<head>
<meta charset="utf-8">
<title>Velmora Trade Hall</title>
<link rel="stylesheet" href="https://fonts.googleapis.com/css2?family=Arimo:wght@400;700&family=Open+Sans:wght@300;400;600;700&family=Oswald:wght@300;500&family=PT+Serif:ital@1&display=swap">
<style>
:root{
  --blue:#2f9fcf;
  --blue-dark:#1d7fae;
  --blue-deep:#0c3347;
  --ink:#2b2b2b;
  --text:#6a6a6a;
  --muted:#8a8a8a;
  --line:#bdbdbd;
  --metal:#e4e4e4;
  --metal-dark:#cfcfcf;
  --white:#ffffff;
  --link:#2b8fc0;
}
*{box-sizing:border-box;margin:0;padding:0}
html,body{width:1200px;height:2251px;overflow:hidden}
body{position:relative;font-family:"Arimo",Arial,sans-serif;color:var(--text);
  background:var(--metal) repeating-linear-gradient(0deg,rgba(255,255,255,.25) 0 1px,rgba(0,0,0,.02) 1px 3px);}
.abs{position:absolute}
a{color:inherit;text-decoration:none}

/* header */
.site-header{left:0;top:0;width:1200px;height:125px}
.brand-name{left:180px;top:66px;font-family:"Open Sans",sans-serif;font-weight:600;font-size:12px;letter-spacing:7px;color:var(--ink);white-space:nowrap}
.login-link{right:180px;top:9px;font-size:9px;color:var(--link);letter-spacing:.5px}
.login-link::before{content:"›";margin-right:8px}
.main-nav{left:632px;top:46px;width:388px;height:24px;border-radius:12px;
  background:linear-gradient(#5cc0e6,#1f86b8);border:1px solid #16608a;display:flex;justify-content:space-around;align-items:center;
  box-shadow:inset 0 1px 0 rgba(255,255,255,.4)}
.main-nav a{color:var(--white);font-family:"Open Sans",sans-serif;font-size:10px;font-weight:600}

/* hero */
.hero{left:0;top:125px;width:1200px;height:356px;
  background:linear-gradient(#3fb0dc 0%,#2a93c2 25%,#0e4a67 60%,#0f5a7e 85%,#3ba9d8 100%)}
.hero-kicker{left:185px;top:49px;font-family:"Open Sans",sans-serif;font-weight:700;font-size:26.5px;line-height:1;color:var(--white);white-space:nowrap}
.hero-kicker span,.hero-sub span{color:#1c2a33}
.hero-title{left:185px;top:78px;font-family:"Oswald",sans-serif;font-weight:500;font-size:58px;line-height:1;color:var(--white);white-space:nowrap}
.hero-sub{left:290px;top:139px;font-family:"Open Sans",sans-serif;font-weight:300;font-size:27px;line-height:1;color:var(--white);white-space:nowrap}
.hero-copy{left:186px;top:195px;width:430px;font-size:11.5px;line-height:16px;color:var(--white)}
.hero-next{left:678px;top:187px;width:36px;height:36px;border-radius:50%;background:#35a8da;box-shadow:0 1px 3px rgba(0,0,0,.4)}
.hero-globe{left:815px;top:62px;width:200px;height:200px;border-radius:50%;
  background:radial-gradient(circle at 35% 35%,#e6e6e6,#7a7a7a 55%,#1a1a1a)}
.hero-actions{left:187px;top:242px;display:flex;gap:9px}
.hero-action{width:90px;height:90px;border-radius:50%;background:#222;color:var(--white);
  display:flex;flex-direction:column;align-items:center;justify-content:center;text-align:center;
  font-family:"Open Sans",sans-serif;font-size:11px;line-height:14px;box-shadow:0 2px 4px rgba(0,0,0,.5)}
.hero-action b{font-size:14px;font-weight:700}
.hero-dots{left:578px;top:340px;display:flex;gap:9px}
.hero-dots i{width:8px;height:8px;border-radius:50%;background:#9bb3c0}
.hero-dots i:last-child{background:#fff}

/* features */
.feature{top:512px;width:225px}
.feature h2{font-family:"Open Sans",sans-serif;font-weight:400;font-size:18px;color:var(--ink);padding-bottom:14px;border-bottom:1px solid var(--line)}
.feature-media{margin-top:16px;width:220px;height:76px;border:2px solid #f2f2f2;box-shadow:0 1px 3px rgba(0,0,0,.3)}
.feature p{margin-top:14px;font-size:11px;line-height:16px;color:var(--text)}
.btn{display:inline-flex;align-items:center;justify-content:center;height:21px;border-radius:11px;
  background:linear-gradient(#5cc0e6,#1f86b8);border:1px solid #16608a;color:var(--white);font-size:8.5px;font-family:"Open Sans",sans-serif}
.feature .btn{margin-top:20px;width:80px}

/* about */
.about{left:0;top:777px;width:1200px;height:285px;border-top:1px solid #c8c8c8;
  background:linear-gradient(#f5f5f5,#c9c9c9)}
.about h2{left:180px;top:29px;width:840px;font-family:"Open Sans",sans-serif;font-weight:400;font-size:19px;color:var(--ink);padding-bottom:14px;border-bottom:1px solid var(--line)}
.about h2 b{font-weight:700}
.about-media{left:180px;top:86px;width:117px;height:83px;background:linear-gradient(#e9e9e9,#9a9a9a)}
.about-copy{left:333px;top:85px;width:688px;font-size:11px;line-height:16px}
.quote-icon{left:180px;top:190px}
.about-quote{left:240px;top:188px;width:760px;font-family:"PT Serif",serif;font-style:italic;font-size:13px;line-height:19px;color:#555}
.about-author{right:180px;top:238px;font-size:11px;font-weight:700;color:#111}

/* market */
.market-title{left:183px;top:1088px;display:flex;align-items:center;gap:12px;font-family:"Open Sans",sans-serif;font-size:18px;color:var(--ink)}
.market-table{left:202px;top:1175px;width:810px;border-collapse:collapse;font-family:"Open Sans",sans-serif;font-size:15px;
  background:linear-gradient(#e3e3e3,#d8d8d8)}
.market-table th{background:var(--blue);color:var(--white);text-align:left;font-weight:600;font-size:17px;height:46px;padding:0 12px;border:1px solid #2480ab}
.market-table td{height:46px;padding:0 12px;color:#555;border:1px solid #9e9e9e}

/* tips */
.tips{left:0;top:1600px;width:1200px;height:116px;border-top:1px solid #bbb;border-bottom:1px solid #bbb;
  background:linear-gradient(#cfcfcf,#dadada)}
.tips-media{left:203px;top:24px;width:40px;height:70px;border-radius:20px 20px 8px 8px;background:radial-gradient(circle at 50% 35%,#8fdcff,#1a7fcf 70%)}
.tips h2{left:290px;top:22px;font-family:"Open Sans",sans-serif;font-weight:400;font-size:20px;color:var(--ink)}
.tips p{left:292px;top:60px;width:720px;font-size:11px;line-height:16px}

/* footer */
.col-title{font-family:"Open Sans",sans-serif;font-weight:400;font-size:18px;color:var(--ink);padding-bottom:14px;border-bottom:1px solid var(--line)}
.posts{left:180px;top:1748px;width:197px}
.post{margin-top:16px}
.post h3{font-size:11px;color:var(--link);font-weight:700}
.post p{margin-top:10px;font-size:11px;line-height:16px}
.contact{left:466px;top:1748px;width:554px}
.field{position:absolute;left:0;width:197px;height:22px;border:1px solid #a9a9a9;background:#e8e8e8;font-size:11px;font-style:italic;color:#999;padding:3px 6px}
.message{position:absolute;left:214px;top:52px;width:338px;height:140px;border:1px solid #a9a9a9;background:#e8e8e8;font-size:11px;font-style:italic;color:#999;padding:4px 6px}
.btn-clear{position:absolute;left:414px;top:211px;width:47px}
.btn-send{position:absolute;left:468px;top:211px;width:85px}
.location{left:466px;top:2013px;width:554px}
.address{margin-top:14px;font-size:11.5px;color:#333;line-height:17px}
.address a{color:var(--link)}
.phones{position:absolute;right:0;top:50px;text-align:left;font-size:11px;line-height:17px;color:#666}

.footer-bar{left:0;top:2138px;width:1200px;height:113px;border-top:1px solid #bdbdbd}
.follow{left:180px;top:34px;width:400px;height:38px;border-radius:19px;border:2px solid #1d6e98;
  background:linear-gradient(#5cc0e6,#1f86b8);display:flex;align-items:center;padding-left:16px;gap:14px}
.follow span{font-family:"Open Sans",sans-serif;font-size:18px;color:var(--white);margin-right:10px}
.social{width:20px;height:20px;border-radius:3px;background:rgba(255,255,255,.85)}
.copyright{right:180px;top:47px;font-size:11.5px;color:#888}
</style>
</head>
<body>

<header class="site-header abs">
  <div class="brand-name abs">VELMORA | TRADE | HALL</div>
  <a class="login-link abs" href="#">LOGIN / REGISTER</a>
  <nav class="main-nav abs">
    <a href="#">ACCOUNT</a><a href="#">BUY / SELL BITCOIN</a><a href="#">ORDER BOOK</a><a href="#">DEPOSIT</a>
  </nav>
</header>

<section class="hero abs">
  <div class="hero-kicker abs">VELMORA TRADE HALL <span>OFFERS YOU</span></div>
  <h1 class="hero-title abs">THE MOST EASIEST WAY</h1>
  <div class="hero-sub abs">TO PLACE IN THE <span>BITCOIN WORLD</span></div>
  <p class="hero-copy abs">Sed ut perspiciatis, unde omnis iste natus error sit voluptatem accusantium doloremque laudantium, totam rem aperiam eaque ipsa, quae ab illo inventore veritatis</p>
  <a class="hero-next abs" href="#" aria-label="Next">
    <svg width="36" height="36" viewBox="0 0 36 36"><path d="M15 11l7 7-7 7" fill="none" stroke="#fff" stroke-width="3"/></svg>
  </a>
  <div class="hero-globe abs" role="img" aria-label="Dark metallic globe"></div>
  <div class="hero-actions abs">
    <a class="hero-action" href="#">what is<b>BITCOIN?</b></a>
    <a class="hero-action" href="#">how to buy<b>BITCOIN?</b></a>
    <a class="hero-action" href="#">how to sell<b>BITCOIN?</b></a>
    <a class="hero-action" href="#">open<b>ACCOUNT</b></a>
  </div>
  <div class="hero-dots abs"><i></i><i></i><i></i></div>
</section>

<section class="feature abs" style="left:180px">
  <h2>Secure</h2>
  <div class="feature-media" role="img" aria-label="Golden padlock with keys" style="background:linear-gradient(90deg,#8a8a8a,#d9c27a 55%,#9a9a9a)"></div>
  <p>Sed ut perspiciatis, unde omnis iste natus error sit voluptatem accusantium dolorem laudantium totam rem aperiam.</p>
  <a class="btn" href="#">READ MORE ›</a>
</section>
<section class="feature abs" style="left:487px">
  <h2>Fast</h2>
  <div class="feature-media" role="img" aria-label="Businessmen running" style="background:linear-gradient(90deg,#d8d8d8,#f4f4f4 50%,#bdbdbd)"></div>
  <p>Sed ut perspiciatis, unde omnis iste natus error sit voluptatem accusantium dolorem laudantium totam rem aperiam.</p>
  <a class="btn" href="#">READ MORE ›</a>
</section>
<section class="feature abs" style="left:795px">
  <h2>Bitcoin</h2>
  <div class="feature-media" role="img" aria-label="Silver bitcoin coin" style="background:linear-gradient(90deg,#4a4a4a,#b5b5b5 55%,#555)"></div>
  <p>Sed ut perspiciatis, unde omnis iste natus error sit voluptatem accusantium dolorem laudantium totam rem aperiam.</p>
  <a class="btn" href="#">READ MORE ›</a>
</section>

<section class="about abs">
  <h2 class="abs">Shortly about <b>Velmora Trade Hall</b></h2>
  <div class="about-media abs" role="img" aria-label="Office building"></div>
  <p class="about-copy abs">Sed ut perspiciatis, unde omnis iste natus error sit voluptatem accusantium doloremque laudantium, totam rem aperiam eaque ipsa, quae ab illo inventore veritatis et quasi architecto beatae vitae dicta sunt, explicabo. Nemo enim ipsam voluptatem, quia voluptas sit, aspernatur aut odit aut fugit, sed quia consequuntur magni dolores eos, qui ratione voluptatem sequi nesciunt, neque porro quisquam est, qui dolorem ipsum, quia dolor sit, amet, consectetur, adipisci velit, sed quia non numquam eius modi tempora incidunt, ut labore et dolore magnam aliquam quaerat voluptatem.</p>
  <svg class="quote-icon abs" width="44" height="38" viewBox="0 0 44 38" aria-hidden="true">
    <rect x="1" y="1" width="42" height="26" rx="5" fill="#2a2a2a"/><path d="M8 26l-2 10 10-10z" fill="#2a2a2a"/>
    <circle cx="13" cy="14" r="2.5" fill="#fff"/><circle cx="22" cy="14" r="2.5" fill="#fff"/><circle cx="31" cy="14" r="2.5" fill="#fff"/>
  </svg>
  <blockquote class="about-quote abs">«Nemo enim ipsam voluptatem, quia voluptas sit, aspernatur aut odit aut fugit, sed quia consequ untur magni dolores qui ratione vel voluptatem sequi nesciunt neque quisquam est.»</blockquote>
  <div class="about-author abs">Jon Ardley, Financial Specialist</div>
</section>

<div class="market-title abs">
  <svg width="44" height="30" viewBox="0 0 44 30" aria-hidden="true"><path d="M2 28l12-14 8 7 16-16" fill="none" stroke="#555" stroke-width="4"/><path d="M30 3h10v10z" fill="#555"/></svg>
  Market Analysis
</div>
<table class="market-table abs">
  <thead><tr><th style="width:166px">Instrument</th><th style="width:126px">Last Price</th><th style="width:160px">Total Volume</th><th style="width:168px">Open Interest</th><th style="width:93px">Bid</th><th>Ask</th></tr></thead>
  <tbody>
    <tr><td>BTC/USD-9.14</td><td>573</td><td>231 954</td><td>95 888</td><td>554</td><td>569</td></tr>
    <tr><td>BTC/USD-4.14</td><td>466</td><td>285 026</td><td>68 275</td><td>460</td><td>470</td></tr>
    <tr><td>BTC/USD-6.14</td><td>508</td><td>44 716</td><td>23 247</td><td>498</td><td>507</td></tr>
    <tr><td>OIL/BTC-04.14</td><td>0.235</td><td>14</td><td>4</td><td>0.2151</td><td>0.2499</td></tr>
    <tr><td>BTC/CNY-6.14</td><td>2 820</td><td>52</td><td>2</td><td>2 570</td><td>3 240</td></tr>
    <tr><td>OIL/USD-04.14</td><td>106.4</td><td>1</td><td>1</td><td>0</td><td>0</td></tr>
  </tbody>
</table>

<section class="tips abs">
  <div class="tips-media abs" role="img" aria-label="Glowing blue light bulb"></div>
  <h2 class="abs">Tips</h2>
  <p class="abs">Sed ut perspiciatis, unde omnis iste natus error sit voluptatem accusantium doloremque laudantium, totam rem aperiam eaque ipsa, quae ab illo inventore veritatis et quasi architecto beatae vitae dicta sunt, explicabo perspiciatis, unde omnis.</p>
</section>

<section class="posts abs">
  <h2 class="col-title">Latest Posts</h2>
  <article class="post"><h3>Post Header</h3><p>Sed ut perspiciatis, unde omnis iste natus error sit voluptatem accusan tium dolorem laudantium. Laudantium, totam rem.</p></article>
  <article class="post"><h3>Post Header</h3><p>Sed ut perspiciatis, unde omnis iste natus error sit voluptatem accusan tium dolorem laudantium. Laudantium, totam rem.</p></article>
  <article class="post"><h3>Post Header</h3><p>Sed ut perspiciatis, unde omnis iste natus error sit voluptatem accusan tium dolorem laudantium. Laudantium, totam rem.</p></article>
</section>

<section class="contact abs">
  <h2 class="col-title">Quick contact form</h2>
  <div class="field" style="top:52px">Full Name</div>
  <div class="field" style="top:91px">Your Email</div>
  <div class="field" style="top:130px">Telephone</div>
  <div class="field" style="top:169px">Subject</div>
  <div class="message">Your message here</div>
  <a class="btn btn-clear" href="#">CLEAR</a>
  <a class="btn btn-send" href="#">SEND MESSAGE</a>
</section>

<section class="location abs">
  <h2 class="col-title">Where we are?</h2>
  <p class="address">Harrowgate House 12 Calder Street London, W2C 4QN United Kingdom<br><span style="color:#777">Email:</span> <a href="#">info@vth.co.uk</a></p>
  <p class="phones">Tel.: + 1 (800) 555 0142<br>Fax: + 1 (800) 555 0187</p>
</section>

<footer class="footer-bar abs">
  <div class="follow abs"><span>Follow us on:</span>
    <i class="social"></i><i class="social"></i><i class="social"></i><i class="social"></i><i class="social"></i><i class="social"></i><i class="social"></i>
  </div>
  <p class="copyright abs">Copyright © 2014 Velmora Trade Hall. All Right Reserved</p>
</footer>

</body>
</html>
```